Design a menu for a Pizza company

I need help designing a color menu for a pizza company. It will be a 9x16" trifold menu (3-panel). I would like to include some photos of pizza, salads, subs, sandwiches, drinks, etc. (no clipart). Attached is an example of an existing menu. I need to make the menu full color. We would like to modernize this menu with full color photos like the attached sample menu. The final files should have editable files so I can edit prices and menu items as needed. I prefer CorelDraw graphics software.

Target Market(s)

General public.

Industry/Entity Type

Restaurant

Font styles to use
Sans Serif

Colors
ec1f27
fffefc
9bcb3b

Requirements
Must have
• Must have photos and editable fonts. I will need to be able to edit the contents of the menu after you provide me with the final files.
Nice to have
• It would be nice to have this menu created in CorelDraw X7 or X8.
Should not have
• Should not have clip art or low resolution photos.

```html
<!DOCTYPE html>
<html lang="en">
<head>
<meta charset="utf-8">
<title>Casa Rossa Kitchen Menu</title>
<link href="https://fonts.googleapis.com/css2?family=Arimo:wght@400;700&family=Caveat:wght@500;700&family=Gochi+Hand&family=Tinos:wght@700&display=swap" rel="stylesheet">
<style>
  :root {
    --red: #ec1f27;
    --cream: #fffefc;
    --green: #9bcb3b;
    --green-dark: #3f9a3a;
    --mint: #d7e4da;
    --ink: #222222;
    --page-bg: #e9e7e3;
    --card: rgba(255, 254, 252, 0.86);
  }
  * { box-sizing: border-box; margin: 0; padding: 0; }
  html, body { width: 1200px; height: 900px; overflow: hidden; }
  body { background: var(--page-bg); font-family: "Arimo", sans-serif; color: var(--ink); }

  .menu {
    position: absolute; left: 30px; top: 45px;
    width: 1140px; height: 810px;
    display: flex;
    box-shadow: 0 10px 30px rgba(0,0,0,0.18);
  }
  .panel { position: relative; width: 380px; height: 810px; overflow: hidden; }

  .photo-bg { position: absolute; inset: 0; }
  .photo-left {
    background: linear-gradient(180deg, #c8683a 0%, #e0a06c 28%, #efe8e0 45%, #f2eeea 100%);
  }
  .photo-middle {
    background: linear-gradient(180deg, #b96a48 0%, #e7ddd4 25%, #efebe7 55%, #8a5a3c 72%, #f1ede9 80%, #ece8e3 100%);
  }

  .card {
    position: absolute; background: var(--card); border-radius: 6px;
    padding: 14px 18px;
  }

  .section-title {
    font-family: "Gochi Hand", cursive;
    font-size: 27px; letter-spacing: 1px; text-transform: uppercase;
    border-bottom: 1.5px solid var(--ink); padding-bottom: 2px; margin-bottom: 4px;
  }
  .section-note {
    font-family: "Caveat", cursive; font-size: 15px; line-height: 1.1;
    text-align: center; margin-bottom: 4px;
  }
  .item {
    display: flex; align-items: baseline; font-size: 12px; line-height: 1.45;
  }
  .item .name { white-space: nowrap; }
  .item .dots { flex: 1; border-bottom: 1px dotted var(--ink); margin: 0 4px; transform: translateY(-3px); }
  .item .price { white-space: nowrap; }

  .fine-print { font-size: 10.5px; font-style: italic; text-align: center; line-height: 1.35; margin-top: 8px; }

  .hours-title { font-weight: 700; font-size: 15px; text-align: center; margin-bottom: 6px; }
  .hours-row { display: flex; justify-content: space-between; font-size: 13px; line-height: 1.5; }

  .soda-table { width: 100%; border-collapse: collapse; font-size: 11px; }
  .soda-table th { font-weight: 400; font-size: 9.5px; text-align: right; }
  .soda-table td { text-align: right; line-height: 1.45; }
  .soda-table td:first-child, .soda-table th:first-child { text-align: left; }

  .subhead { font-family: "Caveat", cursive; font-size: 17px; text-align: center; margin: 4px 0 2px; }

  .credit { font-weight: 700; font-size: 13px; text-align: center; }
  .dine { font-family: "Tinos", serif; font-weight: 700; font-size: 22px; text-align: center; margin-top: 8px; }

  /* cover */
  .cover { background: var(--mint); }
  .cover-photo {
    position: absolute; left: 0; top: 0; width: 380px; height: 290px;
    background: linear-gradient(135deg, #7a2a1e 0%, #c9542c 35%, #e8b36a 60%, #d98a45 80%, #6b3a22 100%);
  }
  .cover-stripes {
    position: absolute; right: 0; top: 290px; width: 36px; height: 520px;
    background: linear-gradient(90deg, #e98a86 0%, #f4dcd6 50%, #9ccf8c 100%);
  }
  .cover-content {
    position: absolute; left: 20px; width: 304px; top: 370px; text-align: center;
  }
  .brand-name {
    font-family: "Arimo", sans-serif; font-weight: 700; font-size: 46px;
    line-height: 1.1; letter-spacing: 2px; text-transform: uppercase; color: var(--red);
  }
  .book-now {
    display: inline-block; margin-top: 42px; padding: 9px 22px;
    border: 2px solid var(--green-dark); color: var(--green-dark);
    font-size: 22px; letter-spacing: 1px;
  }
  .web { margin-top: 28px; font-size: 15px; color: var(--red); }
  .socials { margin-top: 12px; display: flex; justify-content: center; gap: 10px; }
</style>
</head>
<body>
<main class="menu">

  <section class="panel panel-dinners">
    <div class="photo-bg photo-left" role="img" aria-label="Photo of pizza and pasta dishes fading into a flour-dusted wooden table"></div>

    <div class="card" style="left:22px; top:22px; width:336px;">
      <h2 class="section-title">Italian Dinners</h2>
      <p class="section-note">Choice of Dressing:<br>Ranch, French, Italian, Blue Cheese, Thousand Island</p>
      <div class="item"><span class="name">Spaghetti w/ Meat Sauce</span><span class="dots"></span><span class="price">8.99</span></div>
      <div class="item"><span class="name">Spaghetti w/ Meatballs</span><span class="dots"></span><span class="price">9.99</span></div>
      <div class="item"><span class="name">Veal Parmigiana w/ Spaghetti</span><span class="dots"></span><span class="price">9.99</span></div>
      <div class="item"><span class="name">Chicken Parmigiana w/ Spaghetti</span><span class="dots"></span><span class="price">9.99</span></div>
      <div class="item"><span class="name">Eggplant Parmigiana w/ Spaghetti</span><span class="dots"></span><span class="price">9.99</span></div>
      <div class="item"><span class="name">Baked Lasagne</span><span class="dots"></span><span class="price">9.99</span></div>
      <div class="item"><span class="name">Ravioli w/ Meat Sauce</span><span class="dots"></span><span class="price">9.99</span></div>

      <h2 class="section-title" style="margin-top:16px;">Seafood Dinners</h2>
      <p class="section-note">Served with Garlic Bread, French Fries &amp; Salad<br>Choice of Dressing: Ranch, French, Italian, Blue Cheese, Thousand Island</p>
      <div class="item"><span class="name">Shrimp Basket</span><span class="dots"></span><span class="price">8.99</span></div>
      <div class="item"><span class="name">Crab Cake</span><span class="dots"></span><span class="price">10.99</span></div>
      <div class="item"><span class="name">Fish Filet</span><span class="dots"></span><span class="price">10.99</span></div>

      <h2 class="section-title" style="margin-top:16px;">Children's Menu</h2>
      <div class="item"><span class="name">Chicken Tenders w/ French Fries</span><span class="dots"></span><span class="price">5.99</span></div>
      <div class="item"><span class="name">Spaghetti w/ Meat Sauce</span><span class="dots"></span><span class="price">5.99</span></div>
      <div class="item"><span class="name">Ravioli w/ Meat Sauce</span><span class="dots"></span><span class="price">5.99</span></div>
      <div class="item"><span class="name">Shrimp w/ French Fries</span><span class="dots"></span><span class="price">5.99</span></div>
      <div class="item"><span class="name">*Cheeseburger w/ French Fries &amp; small Beverage</span><span class="dots"></span><span class="price">5.99</span></div>
      <p class="fine-print">*These items are cooked to order.<br>*Consuming raw or undercooked meats may increase<br>your risk of foodborne illness.</p>
    </div>

    <div class="card" style="left:22px; top:660px; width:336px;">
      <p class="hours-title">OPEN 7 DAYS A WEEK</p>
      <div class="hours-row"><span>MONDAY - THURSDAY</span><span>10:30 A.M. - 9:30 P.M.</span></div>
      <div class="hours-row"><span>FRIDAY &amp; SATURDAY</span><span>10:30 A.M. - 10:00 P.M.</span></div>
      <div class="hours-row"><span>SUNDAY</span><span>12:00 NOON - 8:00 P.M.</span></div>
    </div>
  </section>

  <section class="panel panel-drinks">
    <div class="photo-bg photo-middle" role="img" aria-label="Photo of tomatoes, olives and chili peppers over a flour-dusted wooden board"></div>

    <div class="card" style="left:22px; top:22px; width:336px;">
      <h2 class="section-title">Soda</h2>
      <table class="soda-table">
        <tr><th></th><th>12 oz.</th><th>16 oz.</th><th>24 oz.</th><th>32 oz.</th></tr>
        <tr><td>PITCHER</td><td></td><td></td><td></td><td>3.99</td></tr>
        <tr><td>COLA</td><td>.99</td><td>1.30</td><td>1.59</td><td>1.99</td></tr>
        <tr><td>LEMON-LIME</td><td>.99</td><td>1.30</td><td>1.59</td><td>1.99</td></tr>
        <tr><td>ROOT BEER</td><td>.99</td><td>1.30</td><td>1.59</td><td>1.99</td></tr>
        <tr><td>DIET COLA</td><td>.99</td><td>1.30</td><td>1.59</td><td>1.99</td></tr>
      </table>

      <h2 class="section-title" style="margin-top:14px;">Beverages</h2>
      <table class="soda-table">
        <tr><th></th><th>16 oz.</th><th>24 oz.</th><th>32 oz.</th></tr>
        <tr><td>ICED TEA</td><td>1.30</td><td>1.59</td><td>1.99</td></tr>
      </table>

      <h2 class="section-title" style="margin-top:14px;">Beer</h2>
      <p class="subhead">Draft</p>
      <div class="item"><span class="name">32 OZ. PITCHER</span><span class="dots"></span><span class="price">6.99</span></div>
      <div class="item"><span class="name">60 OZ. PITCHER</span><span class="dots"></span><span class="price">10.99</span></div>
      <div class="item"><span class="name">RED BARN LAGER</span><span class="dots"></span><span class="price">2.50</span></div>
      <p class="subhead">Bottles</p>
      <div class="item"><span class="name">RED BARN LAGER</span><span class="dots"></span><span class="price">3.25</span></div>
      <div class="item"><span class="name">MILLSTONE</span><span class="dots"></span><span class="price">3.25</span></div>
      <div class="item"><span class="name">MILLSTONE LITE</span><span class="dots"></span><span class="price">3.25</span></div>
      <div class="item"><span class="name">PEAK RIDGE</span><span class="dots"></span><span class="price">3.25</span></div>
      <div class="item"><span class="name">PEAK RIDGE LIGHT</span><span class="dots"></span><span class="price">3.25</span></div>
      <p class="subhead">Imported Bottles</p>
      <div class="item"><span class="name">VAN DORP</span><span class="dots"></span><span class="price">3.75</span></div>
      <div class="item"><span class="name">SOL DORADO</span><span class="dots"></span><span class="price">3.75</span></div>
    </div>

    <div class="card" style="left:22px; top:640px; width:336px; padding:22px 18px;">
      <p class="credit">Major Credit Cards Accepted</p>
      <p class="dine">DINE-IN and CARRY OUT</p>
    </div>
  </section>

  <section class="panel cover">
    <div class="cover-photo" role="img" aria-label="Photo of a pizza on a wooden board with a glass of red wine and fresh vegetables"></div>
    <div class="cover-stripes" role="img" aria-label="Red, white and green striped edge band"></div>

    <div class="cover-content">
      <h1 class="brand-name">Casa Rossa Kitchen</h1>
      <span class="book-now">BOOK NOW</span>
      <p class="web">www.casarossakitchen.com</p>
      <div class="socials">
        <svg width="24" height="24" viewBox="0 0 24 24" aria-hidden="true"><circle cx="12" cy="12" r="12" fill="var(--red)"/></svg>
        <svg width="24" height="24" viewBox="0 0 24 24" aria-hidden="true"><circle cx="12" cy="12" r="12" fill="var(--red)"/></svg>
        <svg width="24" height="24" viewBox="0 0 24 24" aria-hidden="true"><circle cx="12" cy="12" r="12" fill="var(--red)"/></svg>
      </div>
    </div>
  </section>

</main>
</body>
</html>
```